Spring Style Exclusive Shopping Party for women

We need a postcard design for our Spring Shopping Event. Lark Meadow is a women's apparel and accessories store featuring missy, petite and plus sizes. Event is Saturday, April 1 from 9am-10am. Looking for a twist on the spring shopping party idea. Attaching 2 postcards we have previously sent for this event and 2 ideas for what we are looking for in new postcard.

Target Market(s)

women 20+

Industry/Entity Type

Retail

Font styles to use
Serif

Requirements
Must have
• must be eye catching, have the logo, date and time of event,
Nice to have
• woman model

```html
<!DOCTYPE html>
<html lang="en">
<head>
<meta charset="utf-8">
<title>Lark Meadow – Spring Shopping Event Postcard</title>
<link rel="stylesheet" href="https://fonts.googleapis.com/css2?family=Cinzel:wght@400;600&family=Marcellus&family=Open+Sans:ital,wght@0,400;0,600;1,400&display=swap">
<style>
  :root {
    --page-bg: #ececec;
    --card-bg: #ffffff;
    --red: #e53a2c;
    --orange: #e8622a;
    --ink: #111111;
    --panel: rgba(255, 255, 255, 0.86);
  }
  * { margin: 0; padding: 0; box-sizing: border-box; }
  html, body {
    width: 1200px; height: 1200px; overflow: hidden;
    background: var(--page-bg);
  }
  .postcard {
    position: absolute; left: 50px; top: 175px;
    width: 1100px; height: 850px;
    background: var(--card-bg);
    overflow: hidden;
    box-shadow: 0 6px 24px rgba(0,0,0,0.18);
  }
  .brush-background {
    position: absolute; inset: 0;
    background: radial-gradient(ellipse 62% 70% at 42% 42%, #ffffff 0%, #ffffff 45%, #f7b79a 70%, #ee6a3a 86%, #e53a2c 100%);
  }
  .model-photo {
    position: absolute; left: 730px; top: 58px;
    width: 340px; height: 792px;
    border-radius: 160px 160px 0 0;
    background: linear-gradient(180deg, #f4a98c 0%, #e88d6c 100%);
  }
  .brand {
    position: absolute; left: 224px; top: 70px; width: 404px;
    text-align: center;
    font-family: "Cinzel", serif; font-weight: 600;
    font-size: 48px; letter-spacing: 3px; color: var(--ink);
    padding-bottom: 22px;
    border-bottom: 2px solid var(--ink);
  }
  .invite-panel {
    position: absolute; left: 120px; top: 214px;
    width: 585px; height: 636px;
    background: var(--panel);
    box-shadow: -3px 0 8px rgba(0,0,0,0.08);
    text-align: center;
  }
  .headline {
    margin-top: 40px;
    font-family: "Open Sans", sans-serif; font-weight: 600;
    font-size: 60px; color: var(--red); letter-spacing: -0.5px;
  }
  .event-name {
    margin-top: 28px;
    font-family: "Cinzel", serif; font-weight: 400;
    font-size: 35px; line-height: 1.4; color: var(--ink);
  }
  .offer {
    margin-top: 38px;
    font-family: "Marcellus", serif;
    font-size: 104px; line-height: 1; color: var(--orange);
  }
  .offer-note {
    margin-top: 12px;
    font-family: "Cinzel", serif; font-weight: 600;
    font-size: 35px; letter-spacing: 1px; color: var(--orange);
  }
  .date {
    margin-top: 6px;
    font-family: "Open Sans", sans-serif;
    font-size: 37px; color: var(--ink);
  }
  .time {
    margin-top: 6px;
    font-family: "Open Sans", sans-serif; font-style: italic;
    font-size: 31px; color: var(--ink);
  }
</style>
</head>
<body>
  <main class="postcard">
    <div class="brush-background" role="img" aria-label="Painted red, orange and gold brushstroke swirl background"></div>

    <div class="model-photo" role="img" aria-label="Photo of a smiling woman model in spring casual wear"></div>

    <div class="brand">Lark Meadow</div>

    <section class="invite-panel">
      <h1 class="headline">YOU'RE INVITED</h1>
      <p class="event-name">For Spring Shopping<br>Event</p>
      <p class="offer">30% OFF</p>
      <p class="offer-note">Entire Purchase</p>
      <p class="date">Saturday, April 1</p>
      <p class="time">from 9am-10am</p>
    </section>
  </main>
</body>
</html>
```